Brennick Holdings Business Cards

These are professional business cards that are for my family office.
Put fake emails and phone numbers as of now until I finalize those components. This family office controls my families investments, assets, and future. The cards should be professional.
..
.
.
.
I just uploaded another variation of a logo I would like to see as a business card to I am inbeteen which logo to use

Target Market(s)

business

Industry/Entity Type

business

Contact Information for Business Card

Professional, wealth related, finance related.

Requirements
Must have
• Logo

```html
<!DOCTYPE html>
<html lang="en">
<head>
<meta charset="utf-8">
<title>Brennick Holdings – Business Cards</title>
<link rel="stylesheet" href="https://fonts.googleapis.com/css2?family=Cinzel:wght@600&family=Montserrat:wght@300;400;600&display=swap">
<style>
  :root {
    --backdrop: #aaaaaa;
    --navy: #1a1f2a;
    --navy-emblem: #1e2330;
    --navy-text: #2a3040;
    --paper: #eaeaea;
    --ink: #111111;
    --ink-soft: #555555;
    --dot: #a3a3a3;
    --shadow: rgba(60, 40, 40, 0.35);
  }
  * { margin: 0; padding: 0; box-sizing: border-box; }
  html, body {
    width: 1200px;
    height: 1000px;
    overflow: hidden;
    background: var(--backdrop);
  }
  .card {
    position: absolute;
    width: 733px;
    height: 422px;
    border-radius: 22px;
    overflow: hidden;
    box-shadow: 4px 5px 8px var(--shadow);
  }
  .card--front {
    left: 234px;
    top: 57px;
    background: var(--navy);
  }
  .card--front .emblem {
    position: absolute;
    inset: 0;
  }
  .emblem-name {
    font-family: "Cinzel", serif;
    font-weight: 600;
    font-size: 30px;
    letter-spacing: 1px;
    fill: var(--navy-text);
  }
  .card--back {
    left: 230px;
    top: 503px;
    background: var(--paper);
    text-align: center;
    color: var(--ink);
  }
  .wordmark {
    position: absolute;
    left: 0;
    right: 0;
    top: 72px;
    font-family: "Cinzel", serif;
    font-weight: 600;
    font-size: 34px;
    letter-spacing: 0.5px;
    color: var(--ink);
  }
  .wordmark-dot {
    position: absolute;
    left: 538px;
    top: 60px;
    width: 10px;
    height: 10px;
    border-radius: 50%;
    background: var(--dot);
  }
  .holder {
    position: absolute;
    left: 0;
    right: 0;
    top: 218px;
  }
  .holder-name {
    font-family: "Montserrat", sans-serif;
    font-weight: 600;
    font-size: 25px;
    line-height: 30px;
    color: var(--ink);
  }
  .holder-role {
    font-family: "Montserrat", sans-serif;
    font-weight: 400;
    font-size: 11px;
    letter-spacing: 2px;
    margin-top: 1px;
  }
  .contact {
    position: absolute;
    left: 0;
    right: 0;
    top: 287px;
    list-style: none;
    font-family: "Montserrat", sans-serif;
    font-weight: 300;
    font-size: 20px;
    line-height: 24.5px;
    color: var(--ink-soft);
  }
</style>
</head>
<body>
  <section class="card card--front" aria-label="Card front">
    <svg class="emblem" width="733" height="422" viewBox="0 0 733 422" role="img" aria-label="Brennick Holdings emblem">
      <circle cx="553" cy="210" r="270" fill="var(--navy-emblem)"/>
      <text class="emblem-name" x="535" y="222" text-anchor="middle">Brennick Holdings</text>
    </svg>
  </section>

  <section class="card card--back" aria-label="Card back">
    <span class="wordmark-dot" aria-hidden="true"></span>
    <h1 class="wordmark">Brennick Holdings</h1>
    <div class="holder">
      <p class="holder-name">Name Surname</p>
      <p class="holder-role">POSITION</p>
    </div>
    <ul class="contact">
      <li>123 456 7890</li>
      <li>email@website.com</li>
      <li>website.com</li>
    </ul>
  </section>
</body>
</html>
```